Wordpress Design Project

I now need a Wordpress theme for my new business.
The business offers consultancy on Information Management, Knowledge Management, Records Management and Document Management.
The winning designer must be able to set up the site for me on my webspace provided by Tallowbrook Hosting, or talk me through how to do this.
I already have a logo designed which you can see by viewing my profile on here. I am happy to send copies of the original artwork to bidders.
I recently sold my interest in a very similar business, and want a website similar to (but not the same as) the previous company (who are now my competition!) This website can be viewed at www.qardvane.com
Categories will be similar, but I would like everything to be as configurable as possible.
I have a strong preference for clean unfussy design.
I want original design please. Please no templates from free to use sites with stock images... no jigsaw pictures!!!!
Love this one... http://www.felquist.tv/
Please get in touch with any questions.
Updates
Project Deadline Extended
Reason: All of these are too generic (brief says no jigsaw puzzle images), or have copied QDV which is the COMPETITION - so I don't want the site to look like theirs
Project Deadline Extended
Reason: Please keep trying people
Business
Business

```html
<!DOCTYPE html>
<html lang="en">
<head>
<meta charset="utf-8">
<title>Carrowby Professional Services</title>
<link rel="stylesheet" href="https://fonts.googleapis.com/css2?family=PT+Sans:ital,wght@0,400;0,700;1,400&family=PT+Sans+Narrow:wght@700&display=swap">
<style>
:root{
  --page:#f2f0f1;
  --panel:#ffffff;
  --navy:#1f4777;
  --steel:#3b6593;
  --accent:#4683c2;
  --ink:#4a4a4a;
  --body:#666666;
  --rule:#d9d8d9;
  --field:#f4f4f4;
}
*{box-sizing:border-box;margin:0;padding:0}
html,body{width:1191px;height:1200px;overflow:hidden;background:var(--page)}
body{position:relative;font-family:"PT Sans",Arial,sans-serif;color:var(--body);font-size:11px}
a{color:var(--accent);text-decoration:none}
.abs{position:absolute}
.top-bar{left:0;top:0;width:1191px;height:8px;background:var(--navy)}
.brand{left:202px;top:14px;width:150px;text-align:center}
.brand-dot{display:block;width:48px;height:48px;border-radius:50%;background:var(--steel);margin:0 auto 8px}
.brand-name{font-family:"PT Sans",sans-serif;font-weight:700;font-size:22px;letter-spacing:1px;color:var(--navy);line-height:1}
.brand-sub{font-family:"PT Sans",sans-serif;font-weight:700;font-size:8px;letter-spacing:1.6px;color:var(--navy);margin-top:3px}
.nav{left:595px;top:62px;width:401px;display:flex;justify-content:space-between;font-family:"PT Sans Narrow",sans-serif;font-weight:700;font-size:13px;letter-spacing:1.6px;color:var(--ink)}
.nav .current{color:var(--accent)}
.hero{left:180px;top:123px;width:815px;height:311px;background:linear-gradient(135deg,#e9ebee,#cfd3d8 55%,#b9b2ad)}
.section-title{font-family:"PT Sans Narrow",sans-serif;font-weight:700;font-size:18px;letter-spacing:1.6px;color:var(--ink);white-space:nowrap}
.section-title span{color:var(--accent)}
.title-band{height:13px;background:#dcdadc}
.tab{width:0;height:0;border-left:12px solid var(--panel);border-top:22px solid transparent}
.panel{background:var(--panel)}
.bullet{display:inline-block;width:8px;height:8px;border-radius:50%;background:var(--accent);margin-right:5px;vertical-align:0}
.copy{font-size:10.5px;line-height:20.4px;color:var(--body)}
.copy-tight{font-size:10.5px;line-height:17px;color:var(--body)}
.btn{background:var(--steel);color:#fff;font-size:10px;font-weight:700;text-align:center}
.card-photo{width:196px;height:100px}
.card-h{font-size:12px;font-weight:700;color:var(--ink)}
.sub-h{font-size:12px;font-weight:700;color:var(--ink)}
.more{font-size:12px}
.divider{border-left:1px dotted #c4c4c4}
.label{font-size:10.5px;color:var(--accent)}
.field{background:var(--field);border:1px solid #c9c9c9;font-size:10px;font-style:italic;color:#444;padding-left:10px;line-height:24px}
.select-arrow{background:var(--steel)}
.footer{left:0;top:1076px;width:1191px;height:114px;background:#3d6794}
.footer-base{left:0;top:1190px;width:1191px;height:10px;background:var(--navy)}
.foot-text{font-family:Arial,sans-serif;font-size:9.5px;color:#12243d;line-height:20.4px}
.foot-text strong{color:#fff;font-weight:400}
.foot-links{font-family:Arial,sans-serif;font-size:9.5px;line-height:20.4px;color:#12243d;text-align:right}
.foot-links .current{color:#fff}
</style>
</head>
<body>
<div class="abs top-bar"></div>

<div class="abs brand">
  <span class="brand-dot"></span>
  <div class="brand-name">CARROWBY</div>
  <div class="brand-sub">PROFESSIONAL SERVICES</div>
</div>

<nav class="abs nav">
  <span class="current">HOME</span><span>ABOUT</span><span>SERVICES</span><span>FAQ</span><span>BLOG</span><span>CONTACT</span>
</nav>

<div class="abs hero" role="img" aria-label="Photo of consultants reviewing charts and documents at a desk"></div>

<!-- consultancy section -->
<div class="abs section-title" style="left:192px;top:455px">INFORMATION, RECORDS, KNOWLEDGE &amp; DOCUMENT <span>MANAGEMENT CONSULTANCY</span></div>
<div class="abs title-band" style="left:843px;top:457px;width:155px"></div>
<div class="abs tab" style="left:181px;top:468px"></div>
<div class="abs panel" style="left:181px;top:490px;width:402px;height:209px"></div>
<div class="abs copy" style="left:198px;top:501px;width:375px">
  <p><span class="bullet"></span>Lorem ipsum dolor sit amet, consectetur adipiscing elit. Curabitur eu rhoncus sapien. Sed fringilla, neque non mollis sollicitudin, dolor ligula ornare diam, sed iaculis arcu orci vitae lacus. Nunc ultricies tristique elit at egestas.</p>
  <p>Mauris rutrum vulputate arcu <a href="#">ut commodo</a>. Suspendisse ut magna condimentum mauris consequat hendrerit.</p>
  <p>Nulla facilisi. Nulla scelerisque, lacus tempor aliquam lacinia, odio felis <a href="#">aliquet</a> nisl, varius rhoncus tellus justo pellentesque nisl.</p>
</div>
<div class="abs btn" style="left:198px;top:657px;width:87px;height:25px;line-height:25px">read more</div>

<div class="abs panel" style="left:594px;top:490px;width:196px;height:209px"></div>
<div class="abs card-photo" style="left:594px;top:490px;background:linear-gradient(135deg,#d9dde3,#9fb0c4)" role="img" aria-label="Photo of three colleagues looking at a laptop"></div>
<div class="abs card-h" style="left:603px;top:598px">Image Headline One</div>
<div class="abs copy-tight" style="left:604px;top:618px;width:183px">As an investor finding the right start up that has the right potential and the right level of interest for an investor is very difficult. &nbsp;<a href="#">read more →</a></div>

<div class="abs panel" style="left:802px;top:490px;width:196px;height:209px"></div>
<div class="abs card-photo" style="left:802px;top:490px;background:linear-gradient(135deg,#eef0f3,#a9c2dc)" role="img" aria-label="Photo of hands pointing at a printed bar chart"></div>
<div class="abs card-h" style="left:811px;top:598px">Image Headline Two</div>
<div class="abs copy-tight" style="left:812px;top:618px;width:183px">As an investor finding the right start up that has the right potential and the right level of interest for an investor is very difficult. &nbsp;<a href="#">read more →</a></div>

<!-- headline two -->
<div class="abs section-title" style="left:197px;top:732px">HEADLINE <span>TWO</span></div>
<div class="abs title-band" style="left:322px;top:736px;width:399px"></div>
<div class="abs tab" style="left:181px;top:746px"></div>
<div class="abs panel" style="left:181px;top:769px;width:539px;height:225px"></div>
<div class="abs sub-h" style="left:198px;top:789px">Lower Headline One</div>
<div class="abs copy-tight" style="left:199px;top:819px;width:230px"><span class="bullet"></span>Morbi vitae arcu ipsum, id dictum justo. Ut ut enim metus, sed semper magna. Suspendisse dictum eros quam. Vestibulum sodales, dolor sed viverra <a href="#">ullamcorper</a>, tortor dui sodales nisl, molestie tincidunt elit felis at nisl. Mauris vel augue lacus. Cras quis mauris at nisl tincidunt fermentum.significant returns.</div>
<div class="abs more" style="left:204px;top:955px"><a href="#">read more →</a></div>
<div class="abs divider" style="left:451px;top:783px;height:197px"></div>
<div class="abs sub-h" style="left:470px;top:789px">Lower Headline Two</div>
<div class="abs copy-tight" style="left:471px;top:819px;width:238px"><span class="bullet"></span>JNunc ac ante ac mauris lacinia dignissim. Pellentesque habitant morbi tristique senectus et netus et malesuada fames ac turpis egestas liquam eget erat ut nibh.<br>Vestibulum congue et in elit. Quisque dapibus <a href="#">tellus eget</a> turpis suscipit rhoncus. Nam lacus neque, dictum rutrum iaculis nec, pretium et.</div>
<div class="abs more" style="left:471px;top:955px"><a href="#">read more &nbsp;→</a></div>

<!-- find out more -->
<div class="abs section-title" style="left:743px;top:732px">FIND OUT <span>MORE</span></div>
<div class="abs title-band" style="left:875px;top:736px;width:122px"></div>
<div class="abs panel" style="left:733px;top:769px;width:265px;height:225px"></div>
<div class="abs sub-h" style="left:744px;top:788px;width:220px;line-height:19px">If you are interested in our service please add your email adress</div>
<div class="abs label" style="left:745px;top:836px">What area would you like more info on</div>
<div class="abs field" style="left:745px;top:855px;width:242px;height:24px">Information Management</div>
<div class="abs select-arrow" style="left:962px;top:855px;width:25px;height:24px">
  <svg width="25" height="24" viewBox="0 0 25 24"><path d="M8 9h9l-4.5 6z" fill="#fff"/></svg>
</div>
<div class="abs label" style="left:745px;top:891px">Please enter you email address</div>
<div class="abs field" style="left:745px;top:910px;width:212px;height:25px">Enter your email</div>
<div class="abs btn" style="left:963px;top:911px;width:24px;height:23px;line-height:23px">go</div>
<div class="abs sub-h" style="left:745px;top:955px">more info? &nbsp;<a href="#" style="font-weight:400">contact us →</a></div>

<!-- footer -->
<footer class="abs footer"></footer>
<div class="abs foot-text" style="left:180px;top:1089px"><strong>© Copyright 2012</strong> All rights reserved.<br>233 Street Blvd., Second Add.<br>City Name, &nbsp;123456<br>Tel: 0000 1234567</div>
<div class="abs foot-links" style="left:800px;top:1089px;width:81px"><span class="current">Homepage</span><br>About Us<br>Services<br>Contact Us</div>
<div class="abs foot-links" style="left:900px;top:1091px;width:93px">Latest Blog<br>Disclaimer<br>Privacy Policy<br>Social Media</div>
<div class="abs footer-base"></div>
</body>
</html>
```